Data Analytics Irish company needs Stationery Design

We need a stationery design for our data analytics company based in Dublin called 'Quorbeam': we develop innovative web-based corporate applications exploiting advanced Machine Learning and Data Mining techniques.
Like the animal that inspired our company name, the final design should communicate intelligence and passion; on the other hand, we want to keep the highest professional appeal.
We love our current logo and we have tried out several color variations: we prefer solutions (see the logo attached) with white design and dark backgrounds, but we will also be glad to see some designs that follow the colors of the palette of the attached web screenshot.
It Company

```html
<!DOCTYPE html>
<html lang="en">
<head>
<meta charset="utf-8">
<title>Quorbeam Stationery</title>
<link href="https://fonts.googleapis.com/css2?family=Exo+2:wght@400;600&display=swap" rel="stylesheet">
<style>
  :root {
    --bg: #ececec;
    --paper: #ffffff;
    --ink: #2a2a2a;
    --muted: #7a7a7a;
    --brand: #2a8fd6;
    --dark: #111111;
    --faint: #eef1f5;
  }
  * { box-sizing: border-box; margin: 0; padding: 0; }
  html, body { width: 1200px; height: 2400px; overflow: hidden; }
  body { background: var(--bg); font-family: "Exo 2", Arial, sans-serif; color: var(--ink); position: relative; }

  .sheet { position: absolute; background: var(--paper); box-shadow: 0 6px 18px rgba(0,0,0,.12); overflow: hidden; }

  .wordmark { display: flex; align-items: center; gap: 10px; color: var(--brand); font-weight: 600; letter-spacing: .5px; }
  .wordmark .dot { border-radius: 50%; background: var(--brand); flex: none; }

  /* Business card front */
  .card-front { left: 80px; top: 250px; width: 500px; height: 286px; padding: 36px 40px; }
  .card-front .wordmark { font-size: 30px; }
  .card-front .wordmark .dot { width: 26px; height: 26px; }
  .card-front .person { margin-top: 40px; font-weight: 600; font-size: 16px; letter-spacing: 1px; text-transform: uppercase; }
  .card-front .role { font-size: 12px; color: var(--muted); margin-bottom: 12px; }
  .contact-line { display: flex; align-items: center; gap: 8px; font-size: 12px; line-height: 20px; }
  .contact-line .mark { width: 8px; height: 8px; background: var(--brand); }
  .social { position: absolute; right: 36px; bottom: 30px; display: flex; gap: 5px; }
  .social span { width: 14px; height: 14px; background: var(--brand); }

  /* Business card back */
  .card-back { left: 620px; top: 250px; width: 500px; height: 286px; background: var(--dark); display: flex; align-items: center; justify-content: center; }
  .card-back .wordmark { color: var(--paper); font-size: 34px; }
  .card-back .wordmark .dot { width: 30px; height: 30px; }

  /* Letterhead */
  .letterhead { left: 330px; top: 830px; width: 540px; height: 740px; padding: 50px 56px; }
  .letterhead .wordmark { font-size: 30px; }
  .letterhead .wordmark .dot { width: 26px; height: 26px; }
  .letterhead .decor { position: absolute; right: -60px; top: 40px; width: 300px; height: 300px; border-radius: 50%; background: var(--faint); }
  .letter { position: relative; margin-top: 60px; font-size: 11px; line-height: 17px; }
  .letter p { margin-bottom: 12px; max-width: 360px; }
  .letter .subject { font-weight: 600; }
  .signature { width: 110px; height: 34px; background: linear-gradient(90deg, #d8d8d8, #eeeeee); border-radius: 4px; margin: 6px 0 6px; }
  .letter-footer { position: absolute; left: 0; right: 0; bottom: 0; height: 34px; background: var(--dark); color: #cfcfcf; font-size: 10px; display: flex; align-items: center; justify-content: center; gap: 28px; }
  .letter-footer::before { content: ""; position: absolute; left: 0; right: 0; top: -4px; height: 4px; background: var(--brand); }

  /* Envelopes */
  .envelope-front { left: 250px; top: 1690px; width: 700px; height: 310px; padding: 40px 48px; }
  .envelope-front .wordmark { font-size: 32px; }
  .envelope-front .wordmark .dot { width: 28px; height: 28px; }
  .envelope-back { left: 250px; top: 2040px; width: 700px; height: 310px; }
  .envelope-back .flap-band { position: absolute; left: 0; right: 0; top: 0; height: 96px; background: var(--dark); display: flex; align-items: center; justify-content: center; }
  .envelope-back .wordmark { color: #777; font-size: 18px; gap: 8px; }
  .envelope-back .wordmark .dot { width: 14px; height: 14px; background: #777; }
</style>
</head>
<body>

  <section class="sheet card-front">
    <div class="wordmark"><span class="dot"></span>quorbeam</div>
    <div class="person">Dara Kelleher</div>
    <div class="role">Data Scientist</div>
    <div class="contact-line"><span class="mark"></span>01 555 0142</div>
    <div class="contact-line"><span class="mark"></span>hello@quorbeam.io</div>
    <div class="contact-line"><span class="mark"></span>PO Box 214, Dublin 2</div>
    <div class="social"><span></span><span></span><span></span></div>
  </section>

  <section class="sheet card-back">
    <div class="wordmark"><span class="dot"></span>quorbeam</div>
  </section>

  <section class="sheet letterhead">
    <div class="decor"></div>
    <div class="wordmark"><span class="dot"></span>quorbeam</div>
    <div class="letter">
      <p>12 March 2024</p>
      <p>Niamh Byrne, Harbour Lane Analytics</p>
      <p>Dear Niamh,</p>
      <p class="subject">Quarterly Model Review</p>
      <p>Thank you for sharing the latest data set with our team. We have reviewed the results and prepared a short summary.</p>
      <p>The attached report outlines our findings and next steps for the forecasting model.</p>
      <p>If you have any questions, please do not hesitate to contact us.</p>
      <p>Yours faithfully,</p>
      <div class="signature" role="img" aria-label="Handwritten signature"></div>
    </div>
    <footer class="letter-footer">
      <span>01 555 0142</span><span>hello@quorbeam.io</span><span>quorbeam.io</span>
    </footer>
  </section>

  <section class="sheet envelope-front">
    <div class="wordmark"><span class="dot"></span>quorbeam</div>
  </section>

  <section class="sheet envelope-back">
    <div class="flap-band">
      <div class="wordmark"><span class="dot"></span>quorbeam</div>
    </div>
  </section>

</body>
</html>
```